Brivora Collective Business Card Design

We need a business card design for Brivora Collective. We are a healthcare recruiting, wellness and education company. We partner with medical facilities to find quality candidates. We also offer free wellness courses.
The final design should communicate an emphasis on recruiting and wellness
The main purpose of the business card is to utilized it for networking events, give to hospitals, executives, VCs surgery centers and clinics. I want it to be sleek, clean, use of our brand colors and professional.

```html
<!DOCTYPE html>
<html lang="en">
<head>
<meta charset="utf-8">
<title>Brivora Collective – Business Card</title>
<link rel="stylesheet" href="https://fonts.googleapis.com/css2?family=Lato:wght@400;700&family=Montserrat:wght@700&display=swap">
<style>
  :root {
    --stage: #1b1b1b;
    --teal: #025f57;
    --teal-deep: #024a44;
    --teal-bright: #0fb9a4;
    --white: #ffffff;
    --ink-rule: #9bb9b5;
  }
  * { box-sizing: border-box; margin: 0; padding: 0; }
  html, body { width: 1200px; height: 1015px; overflow: hidden; }
  body {
    background: var(--stage);
    position: relative;
    font-family: "Lato", sans-serif;
  }
  .card {
    position: absolute;
    width: 520px;
    height: 297px;
    overflow: hidden;
    box-shadow: 0 18px 40px rgba(0,0,0,.55);
  }
  /* Back of card */
  .card-back { left: 110px; top: 140px; }
  .card-back .pattern-field {
    position: absolute; inset: 0;
    background: linear-gradient(35deg, var(--teal-deep) 0%, var(--teal) 55%, var(--teal-bright) 100%);
  }
  .card-back .back-name {
    position: absolute; left: 0; right: 0; top: 50%;
    transform: translateY(-50%);
    text-align: center;
    color: var(--white);
    font-size: 26px; font-weight: 400; letter-spacing: .5px;
  }
  /* Front of card */
  .card-front { left: 570px; top: 540px; background: var(--white); }
  .brand {
    position: absolute; left: 0; right: 0; top: 62px;
    display: flex; align-items: center; justify-content: center; gap: 14px;
    color: var(--teal);
  }
  .brand-square { width: 30px; height: 30px; background: var(--teal); border-radius: 4px; }
  .brand-name { font-size: 36px; font-weight: 400; letter-spacing: .3px; }
  .info-band {
    position: absolute; left: 0; right: 0; bottom: 0; height: 118px;
    background: var(--teal); color: var(--white);
  }
  .info-band::before {
    content: ""; position: absolute; left: 0; right: 0; top: 5px;
    height: 1.5px; background: var(--white);
  }
  .person { position: absolute; left: 38px; top: 26px; text-align: right; width: 178px; }
  .person-name { font-family: "Montserrat", sans-serif; font-size: 17px; font-weight: 700; letter-spacing: .4px; }
  .person-role { font-size: 13px; margin-top: 2px; }
  .divider { position: absolute; left: 234px; top: 22px; width: 1px; height: 52px; background: var(--ink-rule); opacity: .6; }
  .contacts { position: absolute; left: 252px; top: 18px; list-style: none; font-size: 12.5px; line-height: 19px; }
  .contacts li { display: flex; align-items: center; gap: 7px; }
  .contacts svg { width: 13px; height: 13px; flex: none; }
  .address { position: absolute; left: 0; right: 0; bottom: 14px; text-align: center; font-size: 13px; letter-spacing: .2px; }
</style>
</head>
<body>

  <section class="card card-back" aria-label="Card back">
    <div class="pattern-field" role="img" aria-label="Repeating brand pattern in teal tones"></div>
    <p class="back-name">Brivora Collective</p>
  </section>

  <section class="card card-front" aria-label="Card front">
    <div class="brand">
      <span class="brand-square"></span>
      <span class="brand-name">Brivora Collective</span>
    </div>

    <div class="info-band">
      <div class="person">
        <p class="person-name">ELIAS MARROW</p>
        <p class="person-role">Managing Director</p>
      </div>
      <span class="divider"></span>
      <ul class="contacts">
        <li>
          <svg viewBox="0 0 24 24" fill="none" stroke="currentColor" stroke-width="2.2" stroke-linecap="round" stroke-linejoin="round"><path d="M22 16.9v3a2 2 0 0 1-2.2 2A19.8 19.8 0 0 1 2.1 4.2 2 2 0 0 1 4.1 2h3a2 2 0 0 1 2 1.7c.1 1 .4 1.9.7 2.8a2 2 0 0 1-.5 2.1L8 9.9a16 16 0 0 0 6 6l1.3-1.3a2 2 0 0 1 2.1-.4c.9.3 1.8.6 2.8.7a2 2 0 0 1 1.7 2z"/></svg>
          061-482 730 915
        </li>
        <li>
          <svg viewBox="0 0 24 24" fill="none" stroke="currentColor" stroke-width="2.2" stroke-linejoin="round"><rect x="2" y="5" width="20" height="14" rx="1"/><path d="M2 6l10 7 10-7"/></svg>
          hello@brivoramail.com
        </li>
        <li>
          <svg viewBox="0 0 24 24" fill="none" stroke="currentColor" stroke-width="2"><circle cx="12" cy="12" r="10"/><path d="M2 12h20M12 2a15 15 0 0 1 0 20M12 2a15 15 0 0 0 0 20"/></svg>
          www.brivorahub.com
        </li>
      </ul>
      <p class="address">87, Larkfield Avenue, Westmere, 30918</p>
    </div>
  </section>

</body>
</html>
```